Dariel’s letterhead for local government

I require a letterhead for quarterly communications with constituents. The colours I have used in the past are navy & green (together) so I’m happy to use similar colours for this. Please refer to business card as an example.
The letter must make reference to the position I hold which is as per below
“Clr Dariel Kostovenko OAM”
And the tag line I have used in the past is “Dariel in Darwin”. Although I’m not sure if this would be used in a letterhead or not. Happy for this to be provided as an option.
I would like a photo in the letterhead as I believe face recognition is key as an elected member.

Target Market(s)

Political interests

Industry/Entity Type

Government Office

Font styles to use
Sans Serif

Requirements
Must have
• Politically professional. I have been an elected member for 2 years so it is expected that the letterhead conveys that. The colours of the business card is to be used.
Nice to have
• Background of photos to be manipulated or changed to make me stand out, if possible?
Should not have
• Looked like it’s cropped or undertaken by an amateur designer.

```html
<!DOCTYPE html>
<html lang="en">
<head>
<meta charset="utf-8">
<title>Clr Dariel Kostovenko OAM – Letterhead</title>
<link rel="stylesheet" href="https://fonts.googleapis.com/css2?family=Arimo:ital,wght@0,400;0,700;1,700&family=Open+Sans:wght@400&display=swap">
<style>
  :root {
    --navy: #1f5a91;
    --navy-deep: #24508a;
    --green: #0f9a4a;
    --ink: #333333;
    --paper: #ffffff;
    --backdrop: #eeeeee;
    --photo-top: #8a9bb0;
    --photo-bottom: #3a4250;
  }
  * { box-sizing: border-box; margin: 0; padding: 0; }
  html, body { width: 1200px; height: 840px; overflow: hidden; }
  body { background: var(--backdrop); position: relative; font-family: "Open Sans", sans-serif; }

  .letterhead {
    position: absolute; left: 315px; top: 17px;
    width: 570px; height: 806px;
    background: var(--paper);
    box-shadow: 0 2px 10px rgba(0,0,0,.12);
    overflow: hidden;
  }
  .edge-navy { position: absolute; left: 0; top: 0; width: 15px; height: 100%; background: var(--navy); }
  .edge-green { position: absolute; left: 15px; top: 0; width: 17px; height: 100%; background: var(--green); }

  .masthead { position: absolute; left: 58px; top: 34px; font-family: "Arimo", sans-serif; color: var(--navy); }
  .masthead .title { font-size: 18px; line-height: 1.1; }
  .masthead .surname { font-size: 19px; font-weight: 700; line-height: 1.15; }
  .masthead .honour { font-size: 12px; font-weight: 400; }

  .contact { position: absolute; left: 330px; top: 60px; display: flex; }
  .contact .icons { display: flex; flex-direction: column; gap: 3px; padding-right: 6px; border-right: 1px solid var(--green); }
  .contact .icons svg { width: 9px; height: 9px; display: block; margin: 1px 0; }
  .contact .lines { padding-left: 6px; display: flex; flex-direction: column; gap: 3px; font-size: 8px; color: var(--navy); }
  .contact .lines span { height: 11px; line-height: 11px; }

  .letter-body { position: absolute; left: 66px; top: 188px; width: 410px; font-size: 9.4px; line-height: 1.6; color: var(--ink); }
  .letter-body p { margin-bottom: 14px; }
  .sign-off { position: absolute; left: 98px; top: 480px; font-size: 9.4px; line-height: 1.6; color: var(--ink); }

  .portrait {
    position: absolute; right: 40px; top: 530px; width: 146px; height: 176px;
    background: linear-gradient(180deg, var(--photo-top), var(--photo-bottom));
    border-radius: 70px 70px 0 0;
  }
  .tagline-rule { position: absolute; right: 24px; top: 706px; width: 182px; height: 5px; }
  .tagline-rule .navy { height: 2px; background: var(--navy); }
  .tagline-rule .green { height: 3px; background: var(--green); }
  .tagline { position: absolute; right: 24px; top: 714px; width: 182px; text-align: center; font-family: "Arimo", sans-serif; font-style: italic; font-weight: 700; font-size: 10px; color: var(--navy); }

  .social { position: absolute; left: 120px; top: 722px; display: flex; flex-direction: column; gap: 6px; font-size: 8px; color: var(--navy); }
  .social li { list-style: none; display: flex; align-items: center; gap: 5px; }
  .social .dot { width: 8px; height: 8px; border-radius: 50%; background: var(--navy-deep); }
</style>
</head>
<body>
  <main class="letterhead">
    <div class="edge-navy"></div>
    <div class="edge-green"></div>

    <header class="masthead">
      <div class="title">Clr Dariel</div>
      <div class="surname">Kostovenko <span class="honour">OAM</span></div>
    </header>

    <address class="contact" style="font-style:normal">
      <div class="icons">
        <svg viewBox="0 0 10 10"><path d="M5 0.5a3 3 0 0 1 3 3c0 2.3-3 6-3 6s-3-3.7-3-6a3 3 0 0 1 3-3z" fill="var(--green)"/><circle cx="5" cy="3.5" r="1.1" fill="#fff"/></svg>
        <svg viewBox="0 0 10 10"></svg>
        <svg viewBox="0 0 10 10"><rect x="1" y="2" width="8" height="6" rx="1.2" fill="var(--green)"/><rect x="3" y="3.5" width="4" height="3" fill="#fff"/></svg>
        <svg viewBox="0 0 10 10"><rect x="1" y="2.2" width="8" height="5.6" fill="var(--green)"/><path d="M1 2.4l4 3 4-3" stroke="#fff" stroke-width="0.8" fill="none"/></svg>
        <svg viewBox="0 0 10 10"><circle cx="5" cy="5" r="4" fill="var(--green)"/><circle cx="5" cy="5" r="2" fill="none" stroke="#fff" stroke-width="0.8"/></svg>
      </div>
      <div class="lines">
        <span>Address Line 1</span>
        <span>Address Line 1</span>
        <span>0400 318 226</span>
        <span>dariel@darielindarwin.com</span>
        <span>www.darielindarwin.com</span>
      </div>
    </address>

    <section class="letter-body">
      <p>Dear Customer,</p>
      <p>Lorem ipsum dolor sit amet, consectetur adipiscing elit. Aenean ut ipsum eget massa hendrerit vestibulum vel in velit. Donec pretium neque velit.</p>
      <p>Aliquam porta lectus nec mauris ornare venenatis. Vivamus non est turpis, et cursus sem. Mauris vehicula erat in diam auctor at bibendum nisl lacinia.</p>
      <p>Morbi imperdiet neque vehicula nunc convallis gravida. Vestibulum iaculis pretium placerat. Integer consequat, est sit amet facilisis eleifend, nibh nibh varius orci, eget dapibus arcu dui non purus. Pellentesque in magna mauris. Duis enim sapien, dictum vitae condimentum a, pulvinar vel lacus. Mauris et molestie nibh. Vestibulum vitae nulla at metus elementum porta sit amet interdum elit. Nulla sollicitudin neque eu nulla volutpat congue.</p>
      <p>Etiam pellentesque, velit id dapibus fermentum, turpis sapien ornare dui, ac tincidunt ligula odio congue purus. Nunc sed ante dui, in porta lectus. Cras nec sem lorem. In hac habitasse platea dictumst. Maecenas id diam quis dui porta tristique. Sed id egestas felis. Donec ullamcorper mattis posuere. Phasellus fermentum eleifend tortor vel dapibus. Vestibulum ante ipsum.</p>
    </section>

    <div class="sign-off">Your Sincerely,<br>Managing Director</div>

    <div class="portrait" role="img" aria-label="Portrait photo of Dariel Kostovenko in a dark suit and tie"></div>
    <div class="tagline-rule"><div class="navy"></div><div class="green"></div></div>
    <div class="tagline">Dariel in Darwin</div>

    <ul class="social">
      <li><span class="dot"></span>@DarielKostovenko</li>
      <li><span class="dot"></span>@DarielKostov</li>
      <li><span class="dot"></span>@dariel.kostov</li>
    </ul>
  </main>
</body>
</html>
```